Business Card Design

We need a business card with the contact information above listed on the front. On the rear we would like to list the services we provide. We are a full service beach home property management company. We provide Home Inspections, Building Projects, Kitchen and Bathroom Upgrades, Deck and Porch Construction, Plumbing-Electrical Repairs, Home Winterizing, Rental Damage Repairs, Winter Security Property Checks, Interior and Exterior Painting, Rental Maintenance Service Calls, Exterior Construction Upgrades.
We have been in business since 1998.
Updates

Project Deadline Extended
Reason: Need more time for approvals. President of the company on business trip and need a few more days. Thanks.

Project Deadline Extended
Reason: Need more time to figure out how this works. My designer I was working with stopped contacting me now I may have to start over.

Industry/Entity Type

Property Management

Contact Information for Business Card

Dunmore Services LLC.
41586 Sandpiper Ct. Frankford DE 19871
Owen Dunmore President-Home Inspector Cell 302-555-0148 odunmore@coveshorelane.example
Kevin Dunmore Vice President Cell 302-555-0193 kdunmore@coveshorelane.example
Office Fax 302-555-0172
Check us out on omitted Dunmore Services LLC

Requirements
Must have
• We would like to have a logo designed, open to all suggestions. We are located in a beach community on the Atlantic Ocean in southern Delaware. We would like to convey somehow that they can leave their usually very expensive 2nd home to us and we will take care of everything. Would even entertain a slogan of some kind.

```html
<!DOCTYPE html>
<html lang="en">
<head>
<meta charset="utf-8">
<title>Dunmore Services LLC – Business Card</title>
<link href="https://fonts.googleapis.com/css2?family=Exo:wght@400;500;600&family=Open+Sans:wght@400;600&display=swap" rel="stylesheet">
<style>
  :root {
    --page-bg: #efece6;
    --indigo: #3c3f9f;
    --indigo-deep: #2f3189;
    --sky: #1b9ad8;
    --charcoal: #3a3a3f;
    --silver-light: #fbfbfb;
    --silver-mid: #e3e3e5;
    --silver-dark: #c9c9cc;
    --white: #ffffff;
  }
  * { margin: 0; padding: 0; box-sizing: border-box; }
  html, body {
    width: 1057px; height: 1200px; overflow: hidden;
    background: var(--page-bg);
  }
  .canvas { position: relative; width: 1057px; height: 1200px; }
  .card {
    position: absolute; left: 118px; width: 820px; height: 470px;
    box-shadow: 0 10px 28px rgba(0,0,0,.22);
    overflow: hidden;
  }
  .card--front { top: 95px; background: var(--sky); padding: 20px; }
  .card--back { top: 635px; background: linear-gradient(160deg, var(--silver-light) 0%, var(--silver-mid) 60%, var(--silver-dark) 100%); }

  .front-frame {
    width: 100%; height: 100%;
    border: 8px solid var(--indigo);
    background: radial-gradient(ellipse at 50% 45%, var(--silver-light) 0%, var(--silver-mid) 70%, var(--silver-dark) 100%);
    display: flex; flex-direction: column; align-items: center; justify-content: center;
    padding: 0 40px; text-align: center;
  }
  .company-name {
    font-family: "Exo", sans-serif; font-weight: 500;
    color: var(--indigo); letter-spacing: 1px;
  }
  .front-frame .company-name { font-size: 46px; }
  .slogan {
    font-family: "Exo", sans-serif; font-size: 19px; font-weight: 500;
    color: var(--sky); letter-spacing: 1px; margin-top: 6px;
  }
  .services {
    list-style: none; display: flex; flex-wrap: wrap; justify-content: center;
    gap: 6px 18px; margin-top: 28px; max-width: 660px;
    font-family: "Open Sans", sans-serif; font-size: 13.5px; color: var(--charcoal);
  }
  .services li::before { content: "■"; color: var(--indigo); font-size: 8px; margin-right: 7px; vertical-align: 2px; }
  .since {
    font-family: "Exo", sans-serif; font-size: 14px; letter-spacing: 4px;
    color: var(--indigo); margin-top: 26px; text-transform: uppercase;
  }

  .back-shapes { position: absolute; inset: 0; }
  .back-title { position: absolute; left: 48px; top: 150px; font-size: 40px; }
  .holder {
    position: absolute; left: 48px; top: 248px; color: var(--white);
    font-family: "Exo", sans-serif;
  }
  .holder-name { font-size: 30px; font-weight: 600; letter-spacing: 3px; }
  .holder-role { font-size: 13px; letter-spacing: 2px; margin-top: 4px; }

  .contact-line {
    position: absolute; display: flex; align-items: center; gap: 10px;
    font-family: "Open Sans", sans-serif; font-size: 14px; letter-spacing: .3px;
    white-space: nowrap;
  }
  .contact-line svg { flex: none; }
  .contact-line--address { left: 408px; top: 301px; color: var(--white); }
  .contact-line--phone1 { left: 600px; top: 346px; color: var(--charcoal); }
  .contact-line--phone2 { left: 600px; top: 378px; color: var(--charcoal); }
  .contact-line--mail1 { left: 48px; top: 352px; color: var(--white); }
  .contact-line--vp { left: 48px; top: 386px; color: var(--white); }
  .contact-line--mail2 { left: 48px; top: 420px; color: var(--white); }
</style>
</head>
<body>
<main class="canvas">

  <section class="card card--front" aria-label="Card front">
    <div class="front-frame">
      <h1 class="company-name">Dunmore Services LLC</h1>
      <p class="slogan">Your beach home, in caring hands</p>
      <ul class="services">
        <li>Home Inspections</li>
        <li>Building Projects</li>
        <li>Kitchen &amp; Bathroom Upgrades</li>
        <li>Deck &amp; Porch Construction</li>
        <li>Plumbing-Electrical Repairs</li>
        <li>Home Winterizing</li>
        <li>Rental Damage Repairs</li>
        <li>Winter Security Property Checks</li>
        <li>Interior &amp; Exterior Painting</li>
        <li>Rental Maintenance Service Calls</li>
        <li>Exterior Construction Upgrades</li>
      </ul>
      <p class="since">Since 1998</p>
    </div>
  </section>

  <section class="card card--back" aria-label="Card back">
    <svg class="back-shapes" width="820" height="470" viewBox="0 0 820 470" aria-hidden="true">
      <polygon points="0,232 336,232 392,290 820,290 820,336 392,336 470,470 0,470" fill="var(--indigo)"/>
      <polygon points="392,290 820,290 820,336 392,336" fill="var(--charcoal)"/>
      <polygon points="392,336 820,336 820,408 432,408" fill="#d3d3d6"/>
      <polygon points="336,232 392,290 392,336 350,262" fill="var(--indigo-deep)"/>
    </svg>

    <h2 class="company-name back-title">Dunmore Services LLC</h2>

    <div class="holder">
      <p class="holder-name">OWEN DUNMORE</p>
      <p class="holder-role">PRESIDENT · HOME INSPECTOR</p>
    </div>

    <p class="contact-line contact-line--address">
      <svg width="18" height="18" viewBox="0 0 18 18"><rect width="18" height="18" fill="var(--sky)"/><path d="M9 3.5a3.5 3.5 0 0 0-3.5 3.5c0 2.6 3.5 7 3.5 7s3.5-4.4 3.5-7A3.5 3.5 0 0 0 9 3.5z" fill="var(--white)"/></svg>
      41586 Sandpiper Ct. Frankford DE 19871
    </p>
    <p class="contact-line contact-line--phone1">
      <svg width="18" height="18" viewBox="0 0 18 18"><rect width="18" height="18" fill="var(--sky)"/><rect x="6" y="3.5" width="6" height="11" rx="1" fill="var(--white)"/></svg>
      Cell 302-555-0148
    </p>
    <p class="contact-line contact-line--phone2">
      <svg width="18" height="18" viewBox="0 0 18 18"><rect width="18" height="18" fill="var(--sky)"/><path d="M6 4h2l1 3-1.3 1a6 6 0 0 0 2.3 2.3L11 9l3 1v2a1.5 1.5 0 0 1-1.5 1.5A8.5 8.5 0 0 1 4.5 5.5 1.5 1.5 0 0 1 6 4z" fill="var(--white)"/></svg>
      Office Fax 302-555-0172
    </p>
    <p class="contact-line contact-line--mail1">
      <svg width="18" height="18" viewBox="0 0 18 18"><rect width="18" height="18" fill="var(--white)"/><rect x="4" y="5.5" width="10" height="7" fill="none" stroke="var(--indigo)" stroke-width="1.3"/><path d="M4 5.5l5 4 5-4" fill="none" stroke="var(--indigo)" stroke-width="1.3"/></svg>
      odunmore@coveshorelane.example
    </p>
    <p class="contact-line contact-line--vp">
      <svg width="18" height="18" viewBox="0 0 18 18"><rect width="18" height="18" fill="var(--white)"/><rect x="6" y="3.5" width="6" height="11" rx="1" fill="var(--indigo)"/></svg>
      Kevin Dunmore, VP · 302-555-0193
    </p>
    <p class="contact-line contact-line--mail2">
      <svg width="18" height="18" viewBox="0 0 18 18"><rect width="18" height="18" fill="var(--white)"/><rect x="4" y="5.5" width="10" height="7" fill="none" stroke="var(--indigo)" stroke-width="1.3"/><path d="M4 5.5l5 4 5-4" fill="none" stroke="var(--indigo)" stroke-width="1.3"/></svg>
      kdunmore@coveshorelane.example
    </p>
  </section>

</main>
</body>
</html>
```